Movie Poster Design for a script

I need movie poster for a script . Here is the Synopsis . (the script is registered)

THE LEDGER KEEPER is a comedy set in Boston for the period between Christmas, 1965 and Christmas, 1975.

THE LEDGER KEEPER is a story about Harold, a straight laced corporate accountant who is recruited by the mob to be their new Bean Counter as their previous accountant died un-expectantly. Harold’s life lacks excitement, so Harold is convinced the new challenge would be good for him. The Mob Boss (Mecks) wants Harry (Mecks does not like the name of Harold) to keep doing business the way his family has done business for the past 83 years. Mecks’s direction to Harry is clear- “Make sure we have more cash coming in than going out, do not let me get convicted, and do not get yourself killed. “ Harry takes on the job, but soon realizes the family business in on the brink of failure and Mecks’s arrest is imminent. Harry takes a classic corporate approach to saving the business by implementing cost cutting measures (slashing entertainment expenses, establishing fuel budgets, shifting to lower cost lawyers, seeking competitive bids for “hit men”…) Most of the steps back fire, Harry becomes an accidental thug, he is arrested, and Mecks almost “terminates” him. Harry shares his new, bolder plan which Mecks agrees to hesitantly. Rather than trying to save money doing business illegally, Harry decides to transform the business into a legitimate, legal entity. He determines most the current family business operations have a need in the legal world. He transforms the families money transferring and laundering operation to a armor care business, the mob’s protection operation to a security firm, the black market network to a legal distribution business These transformations face humorous and often disastrous challenges. However, Mecks sticks with the plan and supports Harry as they have formed a tight, un explained bond.
Throughout the story, Detective Corvin, an ambition police detective is close, but unsuccessful in piercing the illegal operations and the pressure of not arresting the now respected business leaders of the legal operation is mind boggling.
The story ends with everything coming a full cycle with Harry, Mecks, Dunne and the Detective.
The story makes you cheer on Harry, love Mecks, and feel sorry for Detective Corvin.
Updates

Project Deadline Extended
Reason: Need more designs that the few I have received.

Target Market(s)

30-50 year old movie goers

Industry/Entity Type

Entertainment

Font styles to use
Other font styles liked:
• 1970's fond

Colors
33a6d7

Requirements
Must have
• see the cover of the movie Crimson Gambit.

```html
<!DOCTYPE html>
<html lang="en">
<head>
<meta charset="utf-8">
<title>The Ledger Keeper – Poster</title>
<link rel="stylesheet" href="https://fonts.googleapis.com/css2?family=Archivo+Black&family=Roboto:wght@300;400&display=swap">
<style>
  :root {
    --ink: #0a0a0a;
    --cyan: #12c3d6;
    --cyan-deep: #0fb2cc;
    --credit-grey: #2a2a2a;
    --bg-light: #ffffff;
    --bg-edge: #8f8f8f;
  }
  html, body {
    margin: 0;
    padding: 0;
    overflow: hidden;
    background: var(--bg-edge);
  }
  .poster {
    position: relative;
    width: 810px;
    height: 1200px;
    overflow: hidden;
    background: radial-gradient(ellipse 520px 640px at 440px 620px, var(--bg-light) 0%, #f4f4f4 45%, #c9c9c9 80%, var(--bg-edge) 100%);
    font-family: "Roboto", Arial, sans-serif;
  }
  .title {
    position: absolute;
    left: 30px;
    top: 14px;
    margin: 0;
    font-family: "Archivo Black", "Arial Black", sans-serif;
    font-weight: 400;
    line-height: 0.82;
    letter-spacing: -2px;
    color: var(--ink);
  }
  .title span { display: block; }
  .title .line-small { font-size: 98px; }
  .title .line-accent { font-size: 124px; color: var(--cyan); }
  .title .line-large { font-size: 124px; }

  .figure-main {
    position: absolute;
    left: 0;
    top: 540px;
    width: 600px;
    height: 660px;
    border-radius: 300px 240px 0 0;
    background: radial-gradient(ellipse at 60% 30%, #111 0%, var(--ink) 70%);
  }
  .figure-small {
    position: absolute;
    left: 528px;
    top: 735px;
    width: 228px;
    height: 465px;
    border-radius: 110px 110px 0 0;
    background: linear-gradient(180deg, var(--cyan) 0%, var(--cyan-deep) 100%);
  }

  .credits {
    position: absolute;
    left: 30px;
    top: 346px;
    width: 720px;
    margin: 0;
    color: var(--credit-grey);
    font-size: 22px;
    font-weight: 400;
    line-height: 26px;
    text-transform: uppercase;
    letter-spacing: 0.3px;
  }
  .credits .role {
    color: var(--cyan);
    font-size: 14px;
    letter-spacing: 0.4px;
  }
</style>
</head>
<body>
<main class="poster">
  <div class="figure-main" role="img" aria-label="Black silhouette of a man in profile, head bowed"></div>
  <div class="figure-small" role="img" aria-label="Cyan silhouette of a smaller figure facing the man"></div>

  <h1 class="title">
    <span class="line-small">THE</span>
    <span class="line-accent">LEDGER</span>
    <span class="line-large">KEEPER</span>
  </h1>

  <p class="credits">
    Name Lastname <span class="role">and</span> Name Director <span class="role">present</span><br>
    Name Lastname <span class="role">and</span> “The Film”<br>
    <span class="role">support by</span> Support Name <span class="role">cinematography by</span><br>
    Cinematographor Name <span class="role">design team</span> Designer Name<br>
    <span class="role">music by</span> Name Lastname <span class="role">special vfx</span> VFX Name <span class="role">and</span> Second Name<br>
    <span class="role">edited by</span> Editor’s Name <span class="role">filmed on location at</span><br>
    Los Angeles California <span class="role">produced by</span> Name Last Name<br>
    <span class="role">written and directed by</span> Name Last Name
  </p>
</main>
</body>
</html>
```